Packaging Design for "Out-beyond" healthy snack

We are a young trading company based in Melaka, Malaysia. Our product range include healthy snack food products such as;
1. Dried fruit (Raisin, Date and Apricot)
2. Nuts (Almond, walnut and Pitstachio)

Our Brand name is - Out-Beyond (registrated mark)
Motto: Healthy snacks that everyone will craved out-Beyond meal time.

Target market segment:
1. Night life business such as Pub, Lounge, Kara-oke
2. Vegetarian and Health food restaurant
3. Appetiser for Premium Restaurant

Packs size : 100g, 250g and 500g

Packing type: Screw Cap Jar (Square L7.5cm X W7.5cm X H9.0cm)

Competitor website:
http://www.brolvexa.com/index.php?ws=ourproducts&cat=Nuts#openproducts

https://kelpo.com/driedfruit/ (For company philosophy)

TRWalsby
trwalsby@mailvexo.com

Ortivel Grove (M) Sdn. Bhd. (owner of Out-beyond brand)

Target Market(s)

Customer that have middle and high income that have disposable budget for healthy and good taste snack in between meal time. Those business man that like to meet client at the night life outlets would enjoy our snacks

Industry/Entity Type

It Company

Font styles to use
Sans Serif

Colors
faa54b
886aae
87cfc6

Requirements
Must have
• 1. Out-beyond as brand name
• 2. Product names area
• 3. Die cut window that let consumer see the product inside
• 4. Nutritional facts and Ingredients
Nice to have
• 1. A attractive logo for "Out-beyond" brand

```html
<!DOCTYPE html>
<html lang="en">
<head>
<meta charset="utf-8">
<title>Out-Beyond Dried Nuts – Label Colourways</title>
<link rel="stylesheet" href="https://fonts.googleapis.com/css2?family=Righteous&family=Oswald:wght@300;400&family=Montserrat:wght@600&display=swap">
<style>
  :root {
    --page-bg: #ffffff;
    --ink-white: #ffffff;
    --brand-dark: #3a2418;
    --panel-black: #000000;
    --panel-purple: #886aae;
    --panel-teal: #87cfc6;
    --panel-orange: #faa54b;
    --nut-light: #d9b98c;
    --nut-mid: #a9683d;
    --nut-dark: #6b3a1f;
  }
  * { margin: 0; padding: 0; box-sizing: border-box; }
  html, body { width: 1000px; height: 1200px; overflow: hidden; background: var(--page-bg); }
  .sheet { position: relative; width: 1000px; height: 1200px; }

  .label { position: absolute; width: 350px; height: 360px; overflow: hidden; }
  .label--black  { left: 90px;  top: 188px; --panel: var(--panel-black);  --brand: var(--ink-white); }
  .label--purple { left: 560px; top: 188px; --panel: var(--panel-purple); --brand: var(--brand-dark); }
  .label--teal   { left: 90px;  top: 778px; --panel: var(--panel-teal);   --brand: var(--brand-dark); }
  .label--orange { left: 560px; top: 778px; --panel: var(--panel-orange); --brand: var(--brand-dark); }

  .label__art { position: absolute; inset: 0; width: 350px; height: 360px; }
  .label__panel { fill: var(--panel); }

  .brand-name {
    position: absolute; left: 26px; top: 62px;
    font-family: "Righteous", sans-serif; font-size: 22px; letter-spacing: 1px;
    color: var(--brand);
  }
  .eyebrow {
    position: absolute; left: 52px; top: 100px;
    font-family: "Montserrat", sans-serif; font-weight: 600; font-size: 10px; letter-spacing: 1.6px;
    color: var(--ink-white);
  }
  .product-name {
    position: absolute; font-family: "Righteous", sans-serif; font-size: 82px; line-height: 1;
    color: var(--ink-white);
    text-shadow: -3px 3px 0 var(--panel), -5px 5px 0 rgba(255,255,255,.85), -7px 7px 0 var(--panel), -9px 9px 0 rgba(255,255,255,.7);
  }
  .product-name--top { left: 66px; top: 112px; }
  .product-name--bottom { left: 104px; top: 190px; transform: rotate(-6deg); transform-origin: left bottom; }

  .tagline {
    position: absolute; left: 100px; top: 270px;
    font-family: "Oswald", sans-serif; font-weight: 300; font-size: 12.5px; line-height: 17px; letter-spacing: .8px;
    color: var(--ink-white); white-space: nowrap;
  }
  .tagline__mark { position: absolute; left: -9px; top: -4px; font-weight: 400; font-size: 20px; }
  .net-weight {
    position: absolute; left: 250px; top: 322px;
    font-family: "Oswald", sans-serif; font-weight: 400; font-size: 11px; letter-spacing: .5px;
    color: var(--ink-white);
  }
</style>
</head>
<body>
<main class="sheet">

  <section class="label label--black">
    <svg class="label__art" viewBox="0 0 350 360" aria-hidden="false">
      <defs>
        <linearGradient id="nuts-window" x1="0" y1="0" x2="1" y2="1">
          <stop offset="0" stop-color="#d9b98c"/>
          <stop offset=".5" stop-color="#a9683d"/>
          <stop offset="1" stop-color="#6b3a1f"/>
        </linearGradient>
      </defs>
      <rect width="350" height="360" fill="url(#nuts-window)" role="img" aria-label="Die-cut window showing mixed almonds, cashews and hazelnuts inside the jar"/>
      <polygon class="label__panel" points="0,0 197,0 298,338 110,338 0,60"/>
    </svg>
    <span class="brand-name">OUT-BEYOND</span>
    <span class="eyebrow">PREMIUM ORGANIC</span>
    <span class="product-name product-name--top">DRIED</span>
    <span class="product-name product-name--bottom">NUTS</span>
    <p class="tagline"><span class="tagline__mark">'</span>THE HEALTHY SNACK<br>THAT EVERYONE CRAVES<br>OUT-BEYOND MEAL TIME</p>
    <span class="net-weight">500G</span>
  </section>

  <section class="label label--purple">
    <svg class="label__art" viewBox="0 0 350 360">
      <rect width="350" height="360" fill="url(#nuts-window)" role="img" aria-label="Die-cut window showing mixed almonds, cashews and hazelnuts inside the jar"/>
      <polygon class="label__panel" points="0,0 197,0 298,338 110,338 0,60"/>
    </svg>
    <span class="brand-name">OUT-BEYOND</span>
    <span class="eyebrow">PREMIUM ORGANIC</span>
    <span class="product-name product-name--top">DRIED</span>
    <span class="product-name product-name--bottom">NUTS</span>
    <p class="tagline"><span class="tagline__mark">'</span>THE HEALTHY SNACK<br>THAT EVERYONE CRAVES<br>OUT-BEYOND MEAL TIME</p>
    <span class="net-weight">500G</span>
  </section>

  <section class="label label--teal">
    <svg class="label__art" viewBox="0 0 350 360">
      <rect width="350" height="360" fill="url(#nuts-window)" role="img" aria-label="Die-cut window showing mixed almonds, cashews and hazelnuts inside the jar"/>
      <polygon class="label__panel" points="0,0 197,0 298,338 110,338 0,60"/>
    </svg>
    <span class="brand-name">OUT-BEYOND</span>
    <span class="eyebrow">PREMIUM ORGANIC</span>
    <span class="product-name product-name--top">DRIED</span>
    <span class="product-name product-name--bottom">NUTS</span>
    <p class="tagline"><span class="tagline__mark">'</span>THE HEALTHY SNACK<br>THAT EVERYONE CRAVES<br>OUT-BEYOND MEAL TIME</p>
    <span class="net-weight">500G</span>
  </section>

  <section class="label label--orange">
    <svg class="label__art" viewBox="0 0 350 360">
      <rect width="350" height="360" fill="url(#nuts-window)" role="img" aria-label="Die-cut window showing mixed almonds, cashews and hazelnuts inside the jar"/>
      <polygon class="label__panel" points="0,0 197,0 298,338 110,338 0,60"/>
    </svg>
    <span class="brand-name">OUT-BEYOND</span>
    <span class="eyebrow">PREMIUM ORGANIC</span>
    <span class="product-name product-name--top">DRIED</span>
    <span class="product-name product-name--bottom">NUTS</span>
    <p class="tagline"><span class="tagline__mark">'</span>THE HEALTHY SNACK<br>THAT EVERYONE CRAVES<br>OUT-BEYOND MEAL TIME</p>
    <span class="net-weight">500G</span>
  </section>

</main>
</body>
</html>
```